Missing Kids Car Doantion Website Design

Please create a new one page website design.

Current site: http://autosforyouth.net/

New WEBSITE address is: VansForLostYouth.org

Use these sites for an idea of what I am looking for. I like these sites best: tiresforsoldiers.org and autosforsoldiers.org

Coding

Coded - Design and coding required

Number of Pages Required

1 page

```html
<!DOCTYPE html>
<html lang="en">
<head>
<meta charset="utf-8">
<title>Seek the Young – Vehicle Donation</title>
<link rel="stylesheet" href="https://fonts.googleapis.com/css2?family=Montserrat:wght@600;700;800&family=Open+Sans:wght@300;400;600;700&display=swap">
<style>
:root{
  --red:#c8102e;
  --red-bright:#e4131b;
  --magenta:#c2185b;
  --ink:#3f3f3f;
  --muted:#555;
  --band:#4a4a4a;
  --blue:#3d6be0;
  --link:#4a6fd8;
  --navy:#1d2a5a;
  --gold:#f2a30f;
  --white:#fff;
  --field:#9a9a9a;
}
*{box-sizing:border-box;margin:0;padding:0}
html,body{width:1200px;height:2980px;overflow:hidden;background:var(--white)}
body{position:relative;font-family:"Open Sans",Arial,sans-serif;color:var(--ink)}
.abs{position:absolute}

/* hero */
.hero{left:0;top:0;width:1200px;height:405px;background:radial-gradient(ellipse at 62% 40%,#8a6a5a 0%,#4a3630 35%,#1c1614 70%,#0d0b0a 100%)}
.brand{left:50px;top:48px;display:flex;align-items:center;gap:10px;font-family:"Open Sans",sans-serif;font-weight:700;font-size:20px;color:var(--gold)}
.brand .dot{width:22px;height:22px;border-radius:50%;background:var(--gold)}
.account{left:888px;top:38px;font-size:13px;color:#bbb}
.social{left:1048px;top:40px;display:flex;gap:9px}
.social span{width:12px;height:12px;border-radius:50%;background:#3a8ee6}
.nav{left:672px;top:366px;display:flex;gap:20px;font-size:15px;color:var(--white)}

/* donate badge */
.donate-red{left:50px;top:186px;width:360px;height:170px;background:var(--red);border-radius:18px 18px 0 0;text-align:center;box-shadow:0 4px 10px rgba(0,0,0,.35)}
.donate-red .phone-ring{position:absolute;left:153px;top:-6px;width:54px;height:54px;border-radius:50%;border:4px solid var(--white);background:var(--red)}
.donate-red h2{position:absolute;left:0;right:0;top:76px;font-family:"Montserrat",sans-serif;font-weight:800;font-size:54px;letter-spacing:4px;color:var(--white)}
.donate-white{left:36px;top:352px;width:390px;height:100px;background:var(--white);text-align:center;padding-top:10px;box-shadow:0 6px 10px rgba(0,0,0,.3);font-family:"Montserrat",sans-serif;font-weight:800;font-size:36px;line-height:42px;color:var(--red)}
.donate-pink{left:50px;top:452px;width:360px;height:138px;background:var(--magenta);border-radius:0 0 14px 14px;text-align:center;color:var(--white);font-family:"Montserrat",sans-serif;font-weight:700;box-shadow:0 6px 12px rgba(0,0,0,.35)}
.donate-pink .pickup{margin-top:20px;font-size:28px}
.donate-pink .tel{margin-top:12px;font-size:36px}

.help{left:470px;top:432px;width:680px;text-align:center;font-family:"Montserrat",sans-serif;color:var(--red)}
.help h1{font-size:92px;font-weight:800;letter-spacing:8px;line-height:100px}
.help p{font-size:36px;font-weight:700;letter-spacing:2px;margin-top:4px}

/* stats */
.tagline{left:0;top:672px;width:1200px;text-align:center;font-family:"Open Sans",sans-serif;font-weight:700;font-size:40px;color:var(--ink);letter-spacing:-1px}
.stat{top:782px;width:340px;text-align:center;font-size:25px;line-height:32px}
.stat b{display:block;font-weight:400;font-size:42px;line-height:48px;color:var(--red)}
.stat a,.more{color:var(--link);font-size:17px;text-decoration:none}

/* band */
.band{left:0;top:995px;width:1200px;height:345px;background:var(--band)}
.band .photo{position:absolute;left:60px;top:20px;width:595px;height:310px;background:linear-gradient(120deg,#6e5b74 0%,#a7958a 40%,#d0c3b4 70%,#8d8478 100%);box-shadow:0 6px 14px rgba(0,0,0,.5)}
.band .copy{position:absolute;left:690px;top:30px;width:420px;text-align:center;color:var(--white)}
.band .alert{font-family:"Montserrat",sans-serif;font-weight:800;font-size:38px;color:var(--red-bright)}
.band .attempt{font-size:24px;margin-top:6px}
.band .most{font-size:44px;margin-top:44px;line-height:52px}
.band .dont{font-weight:700;font-size:32px;line-height:40px}
.band .happen{font-weight:700;font-size:34px;line-height:46px}

/* info rows */
.info-icon{width:120px;text-align:center;font-size:16px;color:#666}
.info-icon .mark{margin:0 auto 10px}
.info-text{width:810px;font-size:21px;line-height:32px;color:#555;font-weight:300}

.strip{left:0;top:1765px;width:1200px;height:97px;background:var(--blue);color:var(--white);text-align:center;font-size:21px;line-height:32px;padding-top:16px;box-shadow:0 5px 8px rgba(0,0,0,.25)}

/* features */
.feature{top:1970px;width:360px;text-align:center;font-size:24px;line-height:34px;color:#555;font-weight:300}
.feature svg{display:block;margin:0 auto 22px}

/* donor form */
.side-bar{top:2245px;width:56px;height:470px;background:var(--blue)}
.donor{left:0;top:2245px;width:1200px;text-align:center}
.donor h3{font-family:"Open Sans",sans-serif;font-weight:400;font-size:31px;letter-spacing:6px;color:var(--navy);margin-top:10px}
.donor p{font-size:17px;color:#555;font-weight:600;margin-top:2px}
.field{position:absolute;left:175px;width:855px;height:40px;border:1.5px solid var(--field);border-radius:8px;padding-left:14px;font-family:"Times New Roman",serif;font-size:20px;color:#555;line-height:37px;background:var(--white)}
.next{left:535px;top:2674px;width:135px;height:34px;background:var(--blue);border:2px solid #1e4fc6;border-radius:3px;color:var(--white);font-size:16px;letter-spacing:2px;text-align:center;line-height:30px}

/* footer */
.foot-brand{left:0;top:2790px;width:1200px;display:flex;justify-content:center;align-items:center;gap:10px;font-weight:700;font-size:26px;color:var(--gold)}
.foot-brand .dot{width:26px;height:26px;border-radius:50%;background:var(--gold)}
.privacy{left:0;top:2882px;width:1200px;text-align:center;font-size:13px;color:#555}
.privacy span{display:inline-block;border-bottom:1px solid #888;padding:0 18px 4px}
.legal{left:90px;top:2912px;width:1020px;text-align:center;font-size:10px;line-height:15px;color:#666}
</style>
</head>
<body>

<section class="abs hero" role="img" aria-label="Close-up photo of a frightened child with an adult hand covering the mouth"></section>
<div class="abs brand"><span class="dot"></span>Seek the Young</div>
<div class="abs account">Login | Register</div>
<div class="abs social" aria-label="Social links"><span></span><span></span><span></span><span></span><span></span></div>
<nav class="abs nav"><span>Home</span><span>About Seek The Young</span><span>Missing Kids</span><span>Contact</span><span>FAQ</span></nav>

<div class="abs donate-red">
  <div class="phone-ring">
    <svg width="46" height="46" viewBox="0 0 24 24" style="margin-top:0"><path d="M7 4.5c.6-.4 1.4-.2 1.7.4l1.4 2.6c.3.6.1 1.3-.4 1.7l-.9.7c.7 1.6 2 2.9 3.6 3.6l.7-.9c.4-.5 1.1-.7 1.7-.4l2.6 1.4c.6.3.8 1.1.4 1.7l-1 1.5c-.5.7-1.4 1-2.2.8C9.7 16.5 7 13.8 5.9 9.5c-.2-.8.1-1.7.8-2.2z" fill="#fff"/></svg>
  </div>
  <h2>DONATE</h2>
</div>
<div class="abs donate-white">YOUR<br>CAR OR BOAT</div>
<div class="abs donate-pink"><div class="pickup">FAST FREE PICKUP</div><div class="tel">888-555-0147</div></div>

<div class="abs help"><h1>HELP</h1><p>FINDING MISSING KIDS</p></div>

<h2 class="abs tagline">IT DOWSN’T HAVE TO COME TO THIS</h2>
<div class="abs stat" style="left:130px"><b>800,000</b>children are reported<br>missing a year<br><a>Read more...</a></div>
<div class="abs stat" style="left:465px"><b>751,000</b>children have seen<br>the Seek the Young program<br><a>Read more...</a></div>
<div class="abs stat" style="left:745px"><b>400+</b>open missing<br>children cases<br><a>Read more...</a></div>

<section class="abs band">
  <div class="photo" role="img" aria-label="Photo of a small boy holding an adult's hand and looking up"></div>
  <div class="copy">
    <div class="alert">Every 10 minutes,</div>
    <div class="attempt">there’s an attempt to abduct a child.</div>
    <div class="most">Most parents</div>
    <div class="dont">don’t think</div>
    <div class="happen">it will happen to them.</div>
  </div>
</section>

<div class="abs info-icon" style="left:126px;top:1428px">
  <div class="mark" role="img" aria-label="Pink child icon" style="width:60px;height:56px;border-radius:50%;background:#e0457b"></div>MISSING KIDS</div>
<p class="abs info-text" style="left:322px;top:1432px">According to the National Youth Safety Office, each year, there are approximately 94,000 missing children, 90,000 runaways, 300 stranger abductions, and 981 family abductions. <span class="more">Read more...</span></p>

<div class="abs info-icon" style="left:126px;top:1565px">
  <div class="mark" role="img" aria-label="Blue question book icon" style="width:60px;height:60px">
    <svg width="60" height="60" viewBox="0 0 60 60"><text x="30" y="24" text-anchor="middle" font-family="Open Sans,sans-serif" font-weight="700" font-size="26" fill="#2f5fcf">?</text><rect x="12" y="30" width="36" height="24" rx="4" fill="#2f5fcf"/></svg>
  </div>LEARN MORE</div>
<p class="abs info-text" style="left:316px;top:1584px">You can help protect the future of children by supporting Seek the Young through your car donation. Your donated vehicle or vessel will be sold at auction and the net proceeds will be returned to Seek the Young. <span class="more">Read more...</span></p>

<div class="abs strip">Your car or boat donation helps support those missing kids. Our operators are standing by 24<br>hours a day, 7 days a week to answer your questions and get your car or boat donation picked up</div>

<div class="abs feature" style="left:30px">
  <svg width="70" height="70" viewBox="0 0 24 24"><path d="M6 3c.7-.5 1.6-.3 2 .4l1.7 3c.4.7.2 1.5-.4 2l-1 .8c.9 2 2.5 3.6 4.5 4.5l.8-1c.5-.6 1.3-.8 2-.4l3 1.7c.7.4.9 1.3.4 2l-1.2 1.8c-.6.8-1.6 1.1-2.6.9C9.5 17.4 6.6 14.5 5.3 8.8c-.2-1 .1-2 .9-2.6z" fill="#1d2a5a"/></svg>
  Fast Free Pickup<br>24hr Response</div>
<div class="abs feature" style="left:345px">
  <svg width="96" height="70" viewBox="0 0 96 70" role="img" aria-label="Savings icon with tick"><ellipse cx="48" cy="36" rx="36" ry="26" fill="none" stroke="#3d6be0" stroke-width="4"/><path d="M30 36l12 12 24-24" fill="none" stroke="#3d6be0" stroke-width="5" stroke-linecap="round"/></svg>
  Tax Deduction<br>Easy To Do!</div>
<div class="abs feature" style="left:750px">
  <svg width="120" height="70" viewBox="0 0 120 70"><path d="M10 22q50 44 100 0" fill="none" stroke="#c2185b" stroke-width="6" stroke-linecap="round"/></svg>
  Running or not<br>No Emission Test Required</div>

<div class="abs side-bar" style="left:0"></div>
<div class="abs side-bar" style="left:1144px"></div>
<section class="abs donor"><h3>DONOR INFORMATION</h3><p>Fill out the form &amp; help protect the future of children.</p></section>
<div class="field" style="top:2340px">First Name</div>
<div class="field" style="top:2392px">Last Name</div>
<div class="field" style="top:2444px">Street Address</div>
<div class="field" style="top:2496px">City</div>
<div class="field" style="top:2548px">State</div>
<div class="field" style="top:2600px">Zip</div>
<div class="abs next">NEXT STEP</div>

<div class="abs foot-brand"><span class="dot"></span>Seek the Young</div>
<div class="abs privacy"><span>Privacy Policy</span></div>
<p class="abs legal">Your donation to autosforyouth.net will benefit Seek the Young, a registered non profit organization that helps find missing children. Seek the Young is not affiliated with any other vehicle donation program or website. Donations are processed through our partners and are tax deductible to the extent allowed by law.</p>

</body>
</html>
```